MVR Flyer Design - Sales Flyer

Using our existing black and red color scheme (logo files attached), we want to create an 8.5 x 16" trifold sales flier template (example attached) for our company. Content/copy is not expected—I only need help with the design/layout. I have shared some images of our operations and people for the flier.
For design themes or other content, you can also look at our website (www.corvanfreight.example) or the attached PowerPoint presentation.
Target Market(s)
Logistics, trucking, storage
Industry/Entity Type
Logistics, trucking, inventory
Look and feel
Each slider illustrates characteristics of the customer's brand and the style your logo design should communicate.

```html
<!DOCTYPE html>
<html lang="en">
<head>
<meta charset="utf-8">
<title>MVR Trifold Sales Flyer</title>
<link href="https://fonts.googleapis.com/css2?family=Poppins:wght@300;400;500;600;700;800&display=swap" rel="stylesheet">
<style>
:root{
  --red:#e42527;
  --red-deep:#c21d22;
  --ink:#2b2b2b;
  --ink-soft:#555;
  --muted:#7a7a7a;
  --paper:#ffffff;
  --mist:#eeeeee;
  --stage:#8c8c8c;
}
*{box-sizing:border-box;margin:0;padding:0}
html,body{width:1200px;height:1027px;overflow:hidden}
body{background:var(--stage);font-family:'Poppins',sans-serif;color:var(--ink);position:relative}
.sheet-label{position:absolute;color:var(--paper);font-weight:700;font-size:21px;letter-spacing:.5px;transform:translateX(-50%);line-height:1}
.panel{position:absolute;background:var(--paper);overflow:hidden}
.panel > svg.art{position:absolute;left:0;top:0;width:100%;height:100%}
.abs{position:absolute}
.brand{position:absolute;display:flex;align-items:center;gap:5px;font-weight:800;color:var(--red);line-height:1;letter-spacing:1px}
.brand .brand-square{display:inline-block;background:var(--ink)}
h2.section-title{position:absolute;font-weight:700;line-height:1.1;white-space:nowrap;color:var(--ink)}
h2.section-title em{font-style:normal;color:var(--red)}
.num-badge{position:absolute;width:26px;height:26px;border-radius:50%;background:var(--red);color:#fff;font-size:11px;display:flex;align-items:center;justify-content:center;font-weight:400}
.rule-title{position:absolute;font-size:7.6px;font-weight:500;line-height:1.15;color:var(--ink)}
.rule-desc{position:absolute;font-size:5.1px;line-height:1.3;color:var(--muted)}
.body-copy{position:absolute;font-size:6.2px;line-height:1.3;color:var(--ink-soft)}
.contact-dot{position:absolute;width:26px;height:26px;border-radius:50%;display:flex;align-items:center;justify-content:center}
.tag-bar{position:absolute;background:var(--ink);color:#fff;font-weight:700;font-size:11px;display:flex;align-items:center;justify-content:flex-end;padding-right:6px;clip-path:polygon(10% 0,100% 0,100% 100%,0 100%)}
.headline{position:absolute;color:#fff;font-weight:800;font-size:16.5px;line-height:1;text-align:right}
.diff-item{position:absolute;font-size:8.6px;line-height:1.27;color:var(--ink-soft);width:150px}
.diff-icon{position:absolute;width:16px;height:16px}
.stat-value{position:absolute;color:var(--red);font-weight:700;font-size:10px;line-height:1}
.stat-label{position:absolute;font-size:5.8px;color:var(--ink-soft);line-height:1}
.pillar-icon{position:absolute;width:34px;height:34px;border-radius:50%;display:flex;align-items:center;justify-content:center}
.pillar-name{position:absolute;font-size:7.2px;font-weight:700;text-align:center;width:80px}
.pillar-copy{position:absolute;font-size:5.2px;line-height:1.28;text-align:center;width:80px;color:var(--ink-soft)}
.pillar-divider{position:absolute;width:0;border-left:1px dotted #999}
.service-photo{position:absolute;width:105px;height:61px;border:1.5px solid var(--red)}
.service-name{position:absolute;width:110px;text-align:center;font-size:6.6px;font-weight:700;line-height:1.15}
.service-copy{position:absolute;width:110px;text-align:center;font-size:4.9px;line-height:1.3;color:var(--ink-soft)}
.back-note{position:absolute;left:24px;border-left:1.6px solid var(--red);padding-left:6px;font-size:7.3px;line-height:1.25;font-weight:500;width:200px}
.back-contact{position:absolute;right:24px;text-align:right;color:#fff;font-size:9px;line-height:1.2}
.back-contact b{font-weight:600}
</style>
</head>
<body>

<div class="sheet-label" style="left:473px;top:38px">OUTSIDE</div>
<div class="sheet-label" style="left:1013px;top:38px">COVER</div>
<div class="sheet-label" style="left:473px;top:512px">INSIDE</div>
<div class="sheet-label" style="left:1013px;top:512px">BACK</div>

<!-- ============ OUTSIDE SPREAD ============ -->
<section class="panel outside-spread" style="left:59px;top:70px;width:798px;height:424px">
  <svg class="art" viewBox="0 0 798 424" aria-hidden="false">
    <defs>
      <linearGradient id="os-mist" x1="0" y1="0" x2="1" y2="1"><stop offset="0" stop-color="#f6f6f6"/><stop offset="1" stop-color="#dcdcdc"/></linearGradient>
      <linearGradient id="os-crew" x1="0" y1="0" x2="1" y2="1"><stop offset="0" stop-color="#9a7a4e"/><stop offset=".5" stop-color="#3e5473"/><stop offset="1" stop-color="#c6b59a"/></linearGradient>
      <linearGradient id="os-lift" x1="0" y1="0" x2="0" y2="1"><stop offset="0" stop-color="#6fa6dc"/><stop offset=".5" stop-color="#c9d9e8"/><stop offset="1" stop-color="#8f7f63"/></linearGradient>
      <linearGradient id="os-loader" x1="0" y1="0" x2="1" y2="1"><stop offset="0" stop-color="#d9d4c4"/><stop offset=".5" stop-color="#c9a23a"/><stop offset="1" stop-color="#77705f"/></linearGradient>
      <linearGradient id="os-pipes" x1="0" y1="0" x2="1" y2="1"><stop offset="0" stop-color="#b9a08f"/><stop offset="1" stop-color="#5d4a40"/></linearGradient>
    </defs>
    <rect x="266" y="0" width="532" height="424" fill="url(#os-mist)"/>
    <polygon points="0,18 47,18 52,47 0,47" fill="var(--red)"/>
    <polygon points="0,175 40,190 151,314 30,424 0,424" fill="url(#os-loader)" role="img" aria-label="Yellow loader handling pipe at the yard"/>
    <polygon points="151,314 248,424 30,424" fill="url(#os-pipes)" role="img" aria-label="Worker handling stacked steel pipe ends"/>
    <polygon points="300,0 531,0 555,75 405,190 290,70" fill="url(#os-crew)" role="img" aria-label="Two crew members in hard hats reviewing a checklist"/>
    <polygon points="553,76 798,76 798,290 460,290 439,160" fill="url(#os-lift)" role="img" aria-label="Large forklift loaded on a flatbed trailer"/>
    <polygon points="676,0 798,0 798,68 742,68" fill="#4a4a44" role="img" aria-label="Pipe yard seen from above"/>
    <polygon points="532,0 676,0 742,68 532,68" fill="#fff"/>
    <rect x="223" y="348" width="264" height="64" fill="#e6e6e6" role="img" aria-label="Line drawing of warehouse, trucks and loading dock"/>
    <polygon points="433,424 679,269 798,269 798,424" fill="var(--red)"/>
    <polygon points="620,305 679,269 760,269 700,305" fill="var(--red-deep)"/>
    <polygon points="728,340 798,275 798,300 750,340" fill="var(--ink)"/>
  </svg>

  <h2 class="section-title" style="left:60px;top:22px;font-size:12.6px">SAFETY EXPECTATIONS &amp;<br>COMPANY CULTURE</h2>

  <div class="num-badge" style="left:19px;top:67px">01</div>
  <div class="rule-title" style="left:50px;top:67px">Stop Work Authority</div>
  <div class="rule-desc" style="left:50px;top:78px;width:85px">Any employee has the right (and responsibility) to halt work if an unsafe condition is discovered</div>
  <div class="num-badge" style="left:141px;top:67px">02</div>
  <div class="rule-title" style="left:172px;top:67px">Fully Documented<br>SOPs/EHS Processes</div>
  <div class="rule-desc" style="left:172px;top:88px;width:85px">We train our employees rigorously and learn continuously</div>
  <div class="num-badge" style="left:19px;top:115px">03</div>
  <div class="rule-title" style="left:50px;top:115px">Secure Facilities</div>
  <div class="rule-desc" style="left:50px;top:126px;width:85px">Fenced/gated access and surveillance; monthly inventory reporting</div>
  <div class="num-badge" style="left:141px;top:115px">04</div>
  <div class="rule-title" style="left:172px;top:115px">Continuous<br>Improvement</div>
  <div class="rule-desc" style="left:172px;top:136px;width:85px">Investigate all near misses, identify root causes and implement corrective action</div>

  <p class="body-copy" style="left:50px;top:172px;width:200px;text-align:center">The health, safety and wellbeing of our employees, contractors, clients, and visitors is of prime importance to the success of our business</p>
  <p class="body-copy" style="left:70px;top:202px;width:190px;text-align:center">We teach our employees from Day 1 that “nothing you do today is more important than going home to your family” and reinforce this by recognizing exemplary safety performance while demonstrating a culture focused on continuous improvement and direct.</p>
  <p class="abs" style="left:119px;top:254px;width:130px;text-align:center;color:var(--red);font-weight:600;font-size:7.4px;line-height:1.22">We have worked safely without an OSHA recordable injury since 2013!</p>

  <div class="brand" style="left:292px;top:212px;font-size:30px">MVR<span class="brand-square" style="width:14px;height:14px"></span></div>

  <div class="contact-dot" style="left:296px;top:256px;background:var(--red)">
    <svg width="13" height="13" viewBox="0 0 24 24"><path d="M6.6 10.8a15 15 0 0 0 6.6 6.6l2.2-2.2c.3-.3.7-.4 1-.2 1.1.4 2.3.6 3.6.6.6 0 1 .4 1 1V20c0 .6-.4 1-1 1A17 17 0 0 1 3 4c0-.6.4-1 1-1h3.5c.6 0 1 .4 1 1 0 1.3.2 2.5.6 3.6.1.3 0 .7-.2 1z" fill="#fff"/></svg>
  </div>
  <div class="contact-dot" style="left:326px;top:256px;background:var(--ink)">
    <svg width="14" height="14" viewBox="0 0 24 24" fill="none" stroke="#fff" stroke-width="1.8"><circle cx="12" cy="12" r="9"/><path d="M3 12h18M12 3c3 3 3 15 0 18M12 3c-3 3-3 15 0 18"/></svg>
  </div>
  <div class="contact-dot" style="left:357px;top:256px;background:var(--red)">
    <svg width="14" height="14" viewBox="0 0 24 24" fill="none" stroke="#fff" stroke-width="1.8"><rect x="3" y="6" width="18" height="12"/><path d="M3 6l9 7 9-7"/></svg>
  </div>
  <div class="abs" style="left:296px;top:287px;font-size:16px;font-weight:500;line-height:1">(555) 014-7185</div>
  <div class="abs" style="left:297px;top:309px;font-size:10.4px;font-weight:500;line-height:1">contactus@corvanfreight.example</div>
  <div class="abs" style="left:297px;top:324px;font-size:10.4px;font-weight:500;line-height:1">www.corvanfreight.example</div>

  <div class="brand" style="left:551px;top:21px;font-size:33px">MVR<span class="brand-square" style="width:15px;height:15px"></span></div>
  <div class="tag-bar" style="left:615px;top:341px;width:165px;height:20px">LOGISTICS REDEFINED</div>
  <div class="headline" style="right:18px;top:366px">TAILORED SOLUTIONS FOR<br>YOUR BUSINESS NEEDS</div>
</section>

<!-- ============ COVER ============ -->
<section class="panel cover" style="left:880px;top:70px;width:266px;height:424px">
  <svg class="art" viewBox="0 0 266 424">
    <defs>
      <linearGradient id="cv-lift" x1="0" y1="0" x2="0" y2="1"><stop offset="0" stop-color="#6fa6dc"/><stop offset=".5" stop-color="#c9d9e8"/><stop offset="1" stop-color="#8f7f63"/></linearGradient>
    </defs>
    <polygon points="0,0 10,0 0,20" fill="#6b7d93" role="img" aria-label="Edge of crew photo"/>
    <rect x="0" y="76" width="266" height="214" fill="url(#cv-lift)" role="img" aria-label="Large forklift loaded on a flatbed trailer"/>
    <polygon points="135,0 266,0 266,68 207,68" fill="#4a4a44" role="img" aria-label="Pipe yard seen from above"/>
    <polygon points="0,386 125,269 266,269 266,424 0,424" fill="var(--red)"/>
    <polygon points="70,320 125,269 200,269 145,320" fill="var(--red-deep)"/>
    <polygon points="196,340 266,275 266,300 218,340" fill="var(--ink)"/>
  </svg>
  <div class="brand" style="left:19px;top:21px;font-size:33px">MVR<span class="brand-square" style="width:15px;height:15px"></span></div>
  <div class="tag-bar" style="left:83px;top:341px;width:165px;height:20px">LOGISTICS REDEFINED</div>
  <div class="headline" style="right:18px;top:366px">TAILORED SOLUTIONS FOR<br>YOUR BUSINESS NEEDS</div>
</section>

<!-- ============ INSIDE SPREAD ============ -->
<section class="panel inside-spread" style="left:58px;top:539px;width:805px;height:427px">
  <svg class="art" viewBox="0 0 805 427">
    <defs>
      <linearGradient id="in-mist" x1="0" y1="0" x2="1" y2="1"><stop offset="0" stop-color="#f7f7f7"/><stop offset="1" stop-color="#e2e2e2"/></linearGradient>
      <linearGradient id="in-crew" x1="0" y1="0" x2="1" y2="0"><stop offset="0" stop-color="#c9a23a"/><stop offset=".45" stop-color="#6c6a60"/><stop offset=".75" stop-color="#33496a"/><stop offset="1" stop-color="#8a6a4e"/></linearGradient>
      <linearGradient id="in-truck" x1="0" y1="0" x2="1" y2="1"><stop offset="0" stop-color="#d8d8d8"/><stop offset="1" stop-color="#6a6a6a"/></linearGradient>
    </defs>
    <rect width="805" height="427" fill="url(#in-mist)"/>
    <rect x="536" y="0" width="269" height="427" fill="#f9f9f9"/>
    <polygon points="0,0 370,0 0,217" fill="url(#in-crew)" role="img" aria-label="Crew in hard hats beside a yellow loader at the pipe yard"/>
    <polygon points="0,222 172,112 178,116 0,238" fill="var(--ink)"/>
    <rect x="0" y="367" width="266" height="54" fill="#e4e4e4" role="img" aria-label="Line drawing of warehouse, trucks and loading dock"/>
    <polygon points="512,427 722,313 805,298 805,427" fill="url(#in-truck)" role="img" aria-label="Grayscale close-up of a truck hauling pipe"/>
    <polygon points="510,427 730,309 742,309 528,427" fill="var(--red)"/>
  </svg>

  <div class="brand" style="left:140px;top:172px;font-size:28px">MVR<span class="brand-square" style="width:13px;height:13px"></span></div>
  <h2 class="section-title" style="left:64px;top:217px;font-size:16px">VISION &amp; <em>PURPOSE</em></h2>

  <div class="pillar-icon" style="left:33px;top:249px;background:var(--red)">
    <svg width="18" height="18" viewBox="0 0 24 24" fill="none" stroke="#fff" stroke-width="2"><path d="M12 3l5 7h-3v8h-4v-8H7z"/><path d="M9 21h6"/></svg>
  </div>
  <div class="pillar-name" style="left:10px;top:287px">VISION</div>
  <p class="pillar-copy" style="left:10px;top:296px">To be the leading provider of innovative and reliable logistics solutions, recognized for unwavering dedication to safety, reliability, and superior customer service.</p>
  <div class="pillar-divider" style="left:97px;top:248px;height:106px"></div>
  <div class="pillar-icon" style="left:123px;top:249px;background:var(--ink)">
    <svg width="18" height="18" viewBox="0 0 24 24" fill="none" stroke="#fff" stroke-width="1.8"><path d="M9 18h6M10 21h4M12 3a6 6 0 0 0-3.5 10.9V16h7v-2.1A6 6 0 0 0 12 3z"/></svg>
  </div>
  <div class="pillar-name" style="left:100px;top:287px">INNOVATION</div>
  <p class="pillar-copy" style="left:100px;top:296px">We leverage cutting edge technologies to streamline supply chains and maximize value while keeping it simple – getting your product to the right place at the right time.</p>
  <div class="pillar-divider" style="left:185px;top:248px;height:106px"></div>
  <div class="pillar-icon" style="left:205px;top:249px;background:var(--red)">
    <svg width="18" height="18" viewBox="0 0 24 24" fill="none" stroke="#fff" stroke-width="1.8"><circle cx="10" cy="7" r="3"/><path d="M4 21v-5a6 6 0 0 1 12 0v5"/><path d="M19 4v5M16.5 6.5h5"/></svg>
  </div>
  <div class="pillar-name" style="left:182px;top:287px">PEOPLE</div>
  <p class="pillar-copy" style="left:182px;top:296px">We are passionate about every job we undertake. You can count on our team to complete each task with integrity, dedication, and enthusiasm.</p>

  <h2 class="section-title" style="left:310px;top:62px;font-size:15px">KEY <em>DIFFERENTIATORS</em></h2>
  <svg class="diff-icon" style="left:304px;top:92px" viewBox="0 0 24 24" fill="none" stroke="var(--red)" stroke-width="1.4"><path d="M2 12l5-4 5 3 5-3 5 4M7 14l3 3M10 13l3 3M13 12l3 3"/></svg>
  <p class="diff-item" style="left:337px;top:88px">Deep industry knowledge and expertise</p>
  <svg class="diff-icon" style="left:309px;top:118px" viewBox="0 0 24 24" fill="none" stroke="var(--red)" stroke-width="1.4"><circle cx="12" cy="12" r="9"/><circle cx="12" cy="12" r="5"/><circle cx="12" cy="12" r="1.5"/><path d="M12 12l8-8"/></svg>
  <p class="diff-item" style="left:337px;top:118px">High volume operation with sustained delivery and inventory accuracy performance &gt;99%</p>
  <svg class="diff-icon" style="left:309px;top:170px" viewBox="0 0 24 24" fill="none" stroke="var(--red)" stroke-width="1.4"><path d="M9 18h6M10 21h4M12 5a5 5 0 0 0-3 9v2h6v-2a5 5 0 0 0-3-9z"/><path d="M12 1v2M4 5l1.5 1.5M20 5l-1.5 1.5"/></svg>
  <p class="diff-item" style="left:337px;top:170px">Quarterly business reviews (QBRs) and monthly inventory reporting</p>
  <svg class="diff-icon" style="left:309px;top:211px" viewBox="0 0 24 24" fill="none" stroke="var(--red)" stroke-width="1.4"><rect x="4" y="4" width="16" height="17"/><path d="M4 9h16M8 2v4M16 2v4M8 14h3M8 17h6"/></svg>
  <p class="diff-item" style="left:337px;top:211px">Monthly cycle counts and spot checks</p>

  <h2 class="section-title" style="left:302px;top:242px;font-size:15px">EXCELLENCE <em>IN ACTION</em></h2>
  <p class="body-copy" style="left:302px;top:264px;width:225px">We have highly skilled personnel utilizing cutting-edge equipment and processes to load/unload, store, and transport your product safely and efficiently – no matter the location.</p>
  <p class="body-copy" style="left:302px;top:297px;width:225px">Our ERP software provides seamless planning and real-time tracking of your products – from source to destination – with full transparency at every step.</p>

  <h2 class="section-title" style="left:302px;top:338px;font-size:15px">CURRENT VOLUMES</h2>
  <div class="stat-value" style="left:302px;top:359px">20,000 Tons</div>
  <div class="stat-label" style="left:302px;top:371px">Monthly Volume</div>
  <div class="stat-value" style="left:385px;top:359px">525+</div>
  <div class="stat-label" style="left:385px;top:371px">Monthly Truckloads</div>
  <div class="stat-value" style="left:302px;top:384px">40+</div>
  <div class="stat-label" style="left:302px;top:396px">Monthly Railcars</div>
  <div class="stat-value" style="left:385px;top:384px">30,000 Tons</div>
  <div class="stat-label" style="left:385px;top:396px">Average in Storage</div>

  <h2 class="section-title" style="left:615px;top:23px;font-size:15px">OUR <em>SERVICES</em></h2>

  <div class="service-photo" role="img" aria-label="Flatbed truck parked at the yard" style="left:563px;top:52px;background:linear-gradient(180deg,#8fb7df,#e8e8e8 55%,#9c8c70)"></div>
  <div class="service-name" style="left:561px;top:117px">Transportation &amp;<br>Forklift/Crane Rentals</div>
  <p class="service-copy" style="left:561px;top:135px">From forklifts to trucking, transloading to inspection, we have top-quality options that support you at each step of the process.</p>
  <div class="service-photo" role="img" aria-label="Aerial view of a pipe storage yard" style="left:681px;top:52px;background:linear-gradient(135deg,#a3917a,#6f7b64 60%,#b5a48c)"></div>
  <div class="service-name" style="left:679px;top:117px">Storage</div>
  <p class="service-copy" style="left:679px;top:128px">Our customized storage solutions let you expand your market reach and strategically position inventory for lower freight costs and efficient distribution.</p>

  <div class="service-photo" role="img" aria-label="Stacked pipe at a rail transload site" style="left:563px;top:173px;background:linear-gradient(180deg,#8fb7df,#dcd6cc 40%,#7a6258)"></div>
  <div class="service-name" style="left:561px;top:238px">Transloading</div>
  <p class="service-copy" style="left:561px;top:249px">Our comprehensive logistics services cover every aspect of rail transportation, from the point of origin to the final destination. We assess the required manpower and utilize the right equipment designed to handle the project from start to finish.</p>
  <div class="service-photo" role="img" aria-label="Inspector in a safety vest checking pipe" style="left:681px;top:173px;background:linear-gradient(135deg,#6d8fa6,#e0783a 50%,#8a8a8a)"></div>
  <div class="service-name" style="left:679px;top:238px">Inspection</div>
  <p class="service-copy" style="left:679px;top:249px">Trust us to ensure the reliability and safety of your OCTG material. We ensure your product is free from defects by performing both visual and non-destructive testing (NDT).</p>
</section>

<!-- ============ BACK ============ -->
<section class="panel back" style="left:883px;top:539px;width:268px;height:427px">
  <svg class="art" viewBox="0 0 268 427">
    <defs>
      <linearGradient id="bk-loader" x1="0" y1="0" x2="1" y2="1"><stop offset="0" stop-color="#9fc3e6"/><stop offset=".4" stop-color="#d08a3a"/><stop offset="1" stop-color="#d9774a"/></linearGradient>
      <linearGradient id="bk-truck" x1="0" y1="0" x2="0" y2="1"><stop offset="0" stop-color="#9fc3e6"/><stop offset=".6" stop-color="#e4e4e4"/><stop offset="1" stop-color="#a89478"/></linearGradient>
    </defs>
    <polygon points="161,0 268,0 268,13 173,13" fill="var(--ink)"/>
    <polygon points="268,85 268,310 95,310 180,178" fill="url(#bk-loader)" role="img" aria-label="Orange loader on red dirt at the yard"/>
    <polygon points="29,184 173,184 101,262 11,262" fill="url(#bk-truck)" role="img" aria-label="Flatbed truck hauling pipe"/>
    <polygon points="29,427 119,313 268,313 268,427" fill="var(--red)"/>
    <polygon points="60,427 82,397 268,397 268,427" fill="var(--ink)"/>
  </svg>
  <div class="brand" style="left:64px;top:28px;font-size:38px">MVR<span class="brand-square" style="width:17px;height:17px"></span></div>
  <p class="back-note" style="top:96px">We understand that every business is unique. Our team will work closely with you to create custom solutions that meet your specific needs and challenges.</p>
  <p class="back-note" style="top:142px">Partner with us for seamless, reliable, and cost-effective logistics solutions tailored to your business needs.</p>
  <div class="back-contact" style="top:331px"><b>Phone</b><br>(555) 014-7185</div>
  <div class="back-contact" style="top:359px"><b>Email</b><br>contactus@corvanfreight.example</div>
  <div class="abs" style="left:94px;top:405px;display:flex;align-items:center;gap:5px;color:#fff;font-size:9.2px;letter-spacing:1.4px">
    <svg width="10" height="10" viewBox="0 0 24 24" fill="none" stroke="#fff" stroke-width="2"><circle cx="12" cy="12" r="9"/><path d="M3 12h18M12 3c3 3 3 15 0 18M12 3c-3 3-3 15 0 18"/></svg>
    corvanfreight.example
  </div>
</section>

</body>
</html>
```